We are starting a new service that will combine local city menus and specials from local restaurants that will then be emailed and printed out on our website.. its a free service to the subscribers and a small charge to the restaurants. We need something to reflect the restaurant industry and to appeal to the general public alike, free to the end user. They sign up and receive daily specials in an email from our site.. not just one city but any one they pick that we service.. We would need links to include. Home, About Us, Sign Up (for free to public), Add Your Restaurant (increase sales and reduce daily calls).. and Contact Us link.. the name of the service is Town Plates at the Ready and website will be townplatesattheready.example. thank you

```html
<!DOCTYPE html>
<html lang="en">
<head>
<meta charset="utf-8">
<title>Town Plates at the Ready</title>
<link rel="stylesheet" href="https://fonts.googleapis.com/css2?family=Ubuntu:wght@400;500&family=Open+Sans:wght@400;600;700&display=swap">
<style>
  :root {
    --page-bg: #ffffff;
    --nav-bg: #222222;
    --nav-active-bg: #080808;
    --nav-text: #9d9d9d;
    --nav-active-text: #ffffff;
    --ink: #333333;
    --ink-dark: #111111;
    --link-blue: #428bca;
    --button-border: #cccccc;
    --hero-dark: #1b1717;
    --hero-warm: #c8693a;
    --hero-wood: #d9a36c;
  }
  * { box-sizing: border-box; margin: 0; padding: 0; }
  html, body { width: 1081px; height: 1200px; overflow: hidden; background: var(--page-bg); }
  body { position: relative; font-family: "Ubuntu", Verdana, sans-serif; color: var(--ink); }

  .site-mark { position: absolute; left: 12px; top: 24px; display: flex; align-items: center; gap: 8px;
    font-family: "Ubuntu", sans-serif; font-size: 13px; font-weight: 500; color: var(--ink-dark); }
  .site-mark__dot { width: 30px; height: 30px; border-radius: 50%; background: #b83a2c; }

  .navbar { position: absolute; left: 0; top: 80px; width: 1081px; height: 54px; background: var(--nav-bg);
    font-family: "Open Sans", Helvetica, sans-serif; }
  .navbar__brand { position: absolute; left: 36px; top: 0; line-height: 54px; font-size: 19px; color: var(--nav-text); letter-spacing: .2px; }
  .navbar__menu { position: absolute; left: 494px; top: 0; display: flex; list-style: none; height: 54px; }
  .navbar__item { height: 54px; line-height: 54px; padding: 0 16px; font-size: 14.5px; color: var(--nav-text); }
  .navbar__item--active { background: var(--nav-active-bg); color: var(--nav-active-text); font-weight: 700; }
  .caret { display: inline-block; margin-left: 5px; vertical-align: middle; border-top: 4px solid; border-left: 4px solid transparent; border-right: 4px solid transparent; }

  .hero { position: absolute; left: 36px; top: 155px; width: 992px; height: 370px; overflow: hidden;
    background:
      radial-gradient(ellipse 60% 40% at 25% 10%, var(--hero-wood), transparent 70%),
      linear-gradient(160deg, var(--hero-warm) 0%, #7a3b24 22%, var(--hero-dark) 45%, #231e1e 100%); }
  .hero__arrow { position: absolute; top: 170px; }
  .hero__arrow--prev { left: 60px; }
  .hero__arrow--next { right: 60px; }
  .hero__dots { position: absolute; left: 471px; top: 320px; display: flex; gap: 6px; }
  .hero__dot { width: 12px; height: 12px; border-radius: 50%; border: 1.5px solid #fff; }
  .hero__dot--active { background: #fff; }

  .feature { position: absolute; top: 588px; width: 310px; text-align: center; }
  .feature--special { left: 44px; }
  .feature--combo { left: 386px; }
  .feature--locate { left: 728px; }
  .feature__photo { width: 158px; height: 158px; border-radius: 50%; margin: 0 auto; }
  .feature--special .feature__photo { background: radial-gradient(circle at 50% 45%, #e8b640, #a9622e 60%, #c9a48f); }
  .feature--combo .feature__photo { background: radial-gradient(circle, #fff 28%, #d8563a 36%, #e7a33a 50%, #4c8a3a 62%, #f4f4f4 72%); }
  .feature--locate .feature__photo { background: linear-gradient(180deg, #d8d8d8 0%, #b3483b 40%, #8a6a4e 62%, #5a5a5a 100%); }
  .feature__title { margin-top: 16px; font-size: 13px; font-weight: 400; color: var(--link-blue); text-transform: uppercase; }
  .feature__text { margin-top: 11px; font-size: 12.7px; line-height: 17.8px; text-align: justify; color: var(--ink-dark); }
  .feature__button { display: inline-block; margin-top: 12px; width: 103px; height: 35px; line-height: 33px;
    border: 1px solid var(--button-border); border-radius: 4px; font-family: "Open Sans", sans-serif; font-size: 15px; color: var(--ink); }

  .footer-col { position: absolute; top: 1022px; width: 240px; color: var(--ink-dark); }
  .footer-col--find { left: 26px; }
  .footer-col--about { left: 291px; }
  .footer-col--menus { left: 556px; }
  .footer-col--connect { left: 821px; }
  .footer-col__heading { font-size: 13px; font-weight: 400; text-transform: uppercase; line-height: 18px; }
  .footer-col__list { margin-top: 8px; padding-left: 42px; list-style: square; font-size: 13.5px; line-height: 19px; }
  .social { list-style: none; margin-top: 6px; }
  .social__item { display: flex; align-items: center; height: 34px; font-size: 13.5px; }
  .social__badge { width: 28px; height: 28px; border-radius: 50%; background: var(--ink-dark); margin-right: 4px; }

  .copyright { position: absolute; left: 0; top: 1160px; width: 1081px; text-align: center; font-size: 13.5px; color: var(--ink-dark); }
</style>
</head>
<body>
  <div class="site-mark"><span class="site-mark__dot"></span>Town Plates at the Ready</div>

  <nav class="navbar">
    <div class="navbar__brand">TOWN PLATES at the READY</div>
    <ul class="navbar__menu">
      <li class="navbar__item navbar__item--active">Home</li>
      <li class="navbar__item">About Us<span class="caret"></span></li>
      <li class="navbar__item">Add Your Restaurant<span class="caret"></span></li>
      <li class="navbar__item">Sign Up</li>
      <li class="navbar__item">Contact Us</li>
    </ul>
  </nav>

  <section class="hero" role="img" aria-label="Close-up photo of a leather restaurant menu cover beside a fork on a wooden table">
    <svg class="hero__arrow hero__arrow--prev" width="22" height="34" viewBox="0 0 22 34"><path d="M18 3 L5 17 L18 31" fill="none" stroke="#fff" stroke-opacity=".85" stroke-width="5"/></svg>
    <svg class="hero__arrow hero__arrow--next" width="22" height="34" viewBox="0 0 22 34"><path d="M4 3 L17 17 L4 31" fill="none" stroke="#fff" stroke-opacity=".85" stroke-width="5"/></svg>
    <div class="hero__dots">
      <span class="hero__dot hero__dot--active"></span><span class="hero__dot"></span><span class="hero__dot"></span>
    </div>
  </section>

  <article class="feature feature--special">
    <div class="feature__photo" role="img" aria-label="Photo of loaded fries with melted cheese"></div>
    <h2 class="feature__title">Daily Special</h2>
    <p class="feature__text">Lorem Ipsum is simply dummy text of the printing and typesetting industry. Lorem Ipsum has been the industry's standard dummy text ever since the 1500s, when an unknown printer took a galley of type and scrambled it to make a type specimen book. It has survived not only five centuries, but also the leap into electronic typesetting, remaining essentially unchanged.</p>
    <span class="feature__button">Read More</span>
  </article>

  <article class="feature feature--combo">
    <div class="feature__photo" role="img" aria-label="Photo of colourful vegetables arranged in a ring"></div>
    <h2 class="feature__title">Menu Combo</h2>
    <p class="feature__text">Lorem Ipsum is simply dummy text of the printing and typesetting industry. Lorem Ipsum has been the industry's standard dummy text ever since the 1500s, when an unknown printer took a galley of type and scrambled it to make a type specimen book. It has survived not only five centuries, but also the leap into electronic typesetting, remaining essentially unchanged.</p>
    <span class="feature__button">Read More</span>
  </article>

  <article class="feature feature--locate">
    <div class="feature__photo" role="img" aria-label="Photo of a painted food truck parked on a street"></div>
    <h2 class="feature__title">Locate a Restaurant</h2>
    <p class="feature__text">Lorem Ipsum is simply dummy text of the printing and typesetting industry. Lorem Ipsum has been the industry's standard dummy text ever since the 1500s, when an unknown printer took a galley of type and scrambled it to make a type specimen book. It has survived not only five centuries, but also the leap into electronic typesetting, remaining essentially unchanged.</p>
    <span class="feature__button">Read More</span>
  </article>

  <footer>
    <div class="footer-col footer-col--find">
      <h3 class="footer-col__heading">Find a Restaurant</h3>
      <ul class="footer-col__list"><li>Europe</li><li>N. America</li><li>Asia</li><li>Australia</li><li>S. America</li></ul>
    </div>
    <div class="footer-col footer-col--about">
      <h3 class="footer-col__heading">About Us</h3>
      <ul class="footer-col__list"><li>Our Blog</li><li>Recipés</li><li>Plates at the Ready</li></ul>
    </div>
    <div class="footer-col footer-col--menus">
      <h3 class="footer-col__heading">All Menus</h3>
      <ul class="footer-col__list"><li>Today's Specials</li><li>Lorem Ipsum</li></ul>
    </div>
    <div class="footer-col footer-col--connect">
      <h3 class="footer-col__heading">Connect With Us</h3>
      <ul class="social">
        <li class="social__item"><span class="social__badge"></span>Friendbook</li>
        <li class="social__item"><span class="social__badge"></span>Talk</li>
        <li class="social__item"><span class="social__badge"></span>Chirper</li>
      </ul>
    </div>
    <p class="copyright">Copyright © Town Plates at the Ready 2014</p>
  </footer>
</body>
</html>
```